Lumaform website scandinavian interior design

Existing website: http://lumaform-example.no/

Webdesign for interior designer Ragna Tvedtholm. The company name is Lumaform. Scandinavian interiør is known to be simple and elegant. The website will be in Norwegian, we are working on the text. The website needs to have a few more pages than just the front page. Here are the different titles of the pages:

1. Hjem
2. Om Lumaform
3. Tjenester og priser
4.. Kontakt oss

There should be Facebook and Instagram icons somewhere at the bottom of the website.

The logo we want to use is attached (pink with black print, see attachment )

We have attached images for inspiration. We want to use some of these colors. The color in the logo, The style should be elegant, modern and delicate.

It is imprtant that the website is user friendly.

Target Market(s)

People who want to decorate their home
Companies and public sector who need to redecorate

Industry/Entity Type

Interior Designer

Coding

Coded - Design and coding required

Number of Pages Required

5+ page

Font styles to use
Other font styles liked:
• see example in the logo breakdown

Requirements
Must have
• Elegant, modern and delicate design
Images of design, see examples attached
Colors similar to the pictures
Should not have
• Too bright colors
Pictures of people

```html
<!DOCTYPE html>
<html lang="en">
<head>
<meta charset="utf-8">
<title>Lumaform – Scandinavian Interior Design</title>
<link href="https://fonts.googleapis.com/css2?family=Cinzel:wght@400;500&family=Lato:wght@300;400&display=swap" rel="stylesheet">
<style>
:root{
  --cream:#fbf7f4;
  --ink:#2b2522;
  --muted:#6d6460;
  --blush:#e8cbbd;
  --sage:#a4aaa4;
  --sage-light:#c9cdc8;
  --white:#ffffff;
  --line:#cfc7c2;
}
*{box-sizing:border-box;margin:0;padding:0}
html,body{width:1200px;height:3836px;overflow:hidden}
body{background:var(--cream);color:var(--ink);font-family:'Lato',sans-serif;position:relative}
.abs{position:absolute}
.serif{font-family:'Cinzel',serif;font-weight:400}
.btn{position:absolute;border:1px solid var(--ink);font-size:11px;letter-spacing:2px;text-transform:uppercase;display:flex;align-items:center;justify-content:center;color:var(--ink);background:transparent}
p.body{font-size:13px;line-height:22px;color:var(--muted);font-weight:300}

/* header */
.site-header{left:0;top:0;width:1200px;height:100px}
.brand{left:100px;top:24px;display:flex;align-items:center;gap:10px}
.brand-mark{width:14px;height:14px;background:var(--blush)}
.brand-name{font-family:'Cinzel',serif;font-size:22px;color:var(--ink)}
.main-nav{right:90px;top:44px;display:flex;gap:52px;font-size:11px;letter-spacing:2px;color:var(--ink)}

/* hero */
.hero-photo{left:372px;top:100px;width:828px;height:492px;background:linear-gradient(135deg,#8a5a3c 0%,#c29a78 40%,#6b3f2a 75%,#3e2a20 100%)}
.hero-title{left:100px;top:332px;font-size:46px;line-height:56px;letter-spacing:3px}
.hero-text{left:100px;top:460px;width:300px}
.hero-btn{left:100px;top:528px;width:124px;height:40px}

/* about */
.about-frame-v{left:496px;top:780px;width:14px;height:600px;background:var(--sage-light)}
.about-frame-h{left:496px;top:1366px;width:704px;height:14px;background:var(--sage-light)}
.about-frame-top{left:180px;top:780px;width:330px;height:14px;background:var(--sage-light)}
.about-photo{left:180px;top:828px;width:400px;height:532px;background:linear-gradient(160deg,#5a3a2c 0%,#8d6650 45%,#e6ddd4 80%,#c9b7a6 100%)}
.about-kicker{left:688px;top:896px;font-size:26px;letter-spacing:3px}
.about-title{left:688px;top:936px;font-size:40px;letter-spacing:3px}
.about-text{left:688px;top:1016px;width:420px}
.about-btn{left:688px;top:1236px;width:124px;height:40px}

/* services */
.services-kicker{left:100px;top:1536px;font-size:22px;letter-spacing:3px}
.services-title{left:100px;top:1568px;font-size:40px;letter-spacing:3px}
.services-text{left:100px;top:1660px;width:320px}
.service-tile{position:absolute;width:324px;height:260px;background:var(--blush);display:flex;flex-direction:column;align-items:center;padding-top:50px;text-align:center}
.service-tile svg{width:60px;height:60px;stroke:var(--ink);fill:none;stroke-width:2}
.service-tile h3{font-family:'Cinzel',serif;font-weight:400;font-size:17px;letter-spacing:2px;margin-top:20px}
.service-tile p{font-size:12px;line-height:19px;color:var(--muted);width:220px;margin-top:14px;font-weight:300}

/* call to action */
.cta-photo{left:0;top:2140px;width:1200px;height:460px;background:linear-gradient(90deg,#8f8a84 0%,#d8d2cb 35%,#c9bfb4 60%,#8a5c5c 100%)}
.cta-veil{left:0;top:2140px;width:1200px;height:460px;background:rgba(40,35,32,.25)}
.cta-title{left:0;top:2316px;width:1200px;text-align:center;color:var(--white);font-size:34px;letter-spacing:3px}
.cta-text{left:400px;top:2372px;width:400px;text-align:center;color:var(--white);font-size:13px;line-height:22px}
.cta-btn{left:536px;top:2446px;width:128px;height:40px;border-color:var(--white);color:var(--white)}

/* contact */
.contact-frame-h{left:0;top:2760px;width:510px;height:14px;background:var(--sage-light)}
.contact-frame-v{left:496px;top:2760px;width:14px;height:600px;background:var(--sage-light)}
.contact-frame-bottom{left:180px;top:3346px;width:330px;height:14px;background:var(--sage-light)}
.contact-photo{left:180px;top:2800px;width:400px;height:530px;background:linear-gradient(170deg,#f3f0ec 0%,#dcd6cf 55%,#b9b3a8 80%,#8f9a7e 100%)}
.contact-title{left:640px;top:2836px;width:460px;text-align:center;font-size:24px;letter-spacing:3px}
.contact-sub{left:640px;top:2874px;width:460px;text-align:center;font-size:12px;color:var(--muted)}
.field-label{position:absolute;font-size:10px;color:var(--muted)}
.field{position:absolute;background:var(--white);border:1px solid var(--line)}
.submit-btn{left:640px;top:3214px;width:460px;height:40px}

/* footer */
.site-footer{left:0;top:3460px;width:1200px;height:376px;background:var(--sage);color:var(--white)}
.footer-brand{left:100px;top:82px;display:flex;align-items:center;gap:10px}
.footer-brand .brand-mark{background:var(--white)}
.footer-brand .brand-name{color:var(--white);font-size:28px}
.footer-head{position:absolute;top:80px;font-family:'Cinzel',serif;font-size:18px;letter-spacing:2px}
.footer-list{position:absolute;top:124px;font-size:12px;line-height:22px;list-style:none}
.contact-list li{display:flex;align-items:center;gap:10px}
.contact-list svg{width:12px;height:12px;stroke:var(--white);fill:none;stroke-width:1.6}
.social{position:absolute;top:124px;left:888px;display:flex;gap:14px}
.social span{width:28px;height:28px;border-radius:50%;background:var(--white);opacity:.9}
.footer-rule{left:100px;top:300px;width:1000px;height:1px;background:rgba(255,255,255,.5)}
.copyright{left:0;top:320px;width:1200px;text-align:center;font-size:11px}
</style>
</head>
<body>

<header class="site-header abs">
  <div class="brand abs"><span class="brand-mark"></span><span class="brand-name">Lumaform</span></div>
  <nav class="main-nav abs"><span>HOME</span><span>ABOUT LUMAFORM</span><span>SERVICES &amp; PRICES</span><span>CONTACT US</span><span>EN ▾</span></nav>
</header>

<section class="hero">
  <div class="hero-photo abs" role="img" aria-label="Warm living room with leather sofas and wooden ceiling"></div>
  <h1 class="hero-title abs serif">INNOVATIVE<br>INTERIOR DESIGN</h1>
  <p class="hero-text abs body">Lorem Ipsum is simply dummy text of the printing and typesetting industry.</p>
  <a class="hero-btn btn">Contact us</a>
</section>

<section class="about">
  <div class="about-frame-top abs"></div>
  <div class="about-frame-v abs"></div>
  <div class="about-frame-h abs"></div>
  <div class="about-photo abs" role="img" aria-label="Cosy corner with rattan chair, throw and stone wall"></div>
  <h2 class="about-kicker abs serif">ABOUT</h2>
  <h2 class="about-title abs serif">LUMAFORM</h2>
  <div class="about-text abs">
    <p class="body">Lorem Ipsum is simply dummy text of the printing and typesetting industry. Lorem Ipsum has been the industry's standard dummy text ever since the 1500s, when an unknown printer took a galley of type and scrambled it to make a type specimen book.</p>
    <p class="body" style="margin-top:16px">It has survived not only five centuries, but also the leap into electronic typesetting, remaining essentially unchanged.</p>
  </div>
  <a class="about-btn btn">Read more</a>
</section>

<section class="services">
  <h2 class="services-kicker abs serif">LUMAFORM</h2>
  <h2 class="services-title abs serif">SERVICES</h2>
  <div class="services-text abs">
    <p class="body">Lorem Ipsum is simply dummy text of the printing and typesetting industry. Lorem Ipsum has been the industry's standard dummy text ever since the 1500s, when an unknown printer took a galley of type and scrambled it to make a type specimen book.</p>
    <p class="body" style="margin-top:16px">It has survived not only five centuries, but also the leap into electronic typesetting, remaining essentially unchanged.</p>
  </div>

  <div class="service-tile" style="left:468px;top:1520px">
    <svg viewBox="0 0 60 60"><path d="M18 30 Q18 8 30 8 Q42 8 42 30 Z"/><path d="M16 30 H44 V36 H16 Z"/><path d="M20 36 L16 54 M40 36 L44 54"/></svg>
    <h3>INTERIOR DESIGN</h3>
    <p>Lorem ipsum is simply dummy text of the printing and typesetting industry.</p>
  </div>
  <div class="service-tile" style="left:796px;top:1520px">
    <svg viewBox="0 0 60 60"><path d="M30 4 V16"/><circle cx="30" cy="20" r="4"/><path d="M10 30 Q30 44 50 30"/><path d="M30 24 V44"/><circle cx="10" cy="26" r="4"/><circle cx="50" cy="26" r="4"/><circle cx="30" cy="48" r="4"/></svg>
    <h3>DECORATIVE SERVICE</h3>
    <p>Lorem ipsum is simply dummy text of the printing and typesetting industry.</p>
  </div>
  <div class="service-tile" style="left:468px;top:1800px">
    <svg viewBox="0 0 60 60"><rect x="6" y="8" width="48" height="44"/><path d="M6 30 H28 V8 M28 40 V52 M36 30 H54 M20 30 V42"/></svg>
    <h3>SPACE PLANNING</h3>
    <p>Lorem ipsum is simply dummy text of the printing and typesetting industry.</p>
  </div>
  <div class="service-tile" style="left:796px;top:1800px">
    <svg viewBox="0 0 60 60"><circle cx="30" cy="22" r="14"/><circle cx="18" cy="30" r="8"/><circle cx="42" cy="30" r="8"/><path d="M30 30 V56 M22 56 H38"/></svg>
    <h3>PROJECT MANAGEMENT</h3>
    <p>Lorem ipsum is simply dummy text of the printing and typesetting industry.</p>
  </div>
</section>

<section class="cta">
  <div class="cta-photo abs" role="img" aria-label="Bright open kitchen and dining room with sofa"></div>
  <div class="cta-veil abs"></div>
  <h2 class="cta-title abs serif">WANT YOU DECORATE YOUR INTERIOR?</h2>
  <p class="cta-text abs">Lorem Ipsum is simply dummy text of the printing and typesetting industry. Lorem Ipsum has been the standard text since the 1500s.</p>
  <a class="cta-btn btn">Contact us</a>
</section>

<section class="contact">
  <div class="contact-frame-h abs"></div>
  <div class="contact-frame-v abs"></div>
  <div class="contact-frame-bottom abs"></div>
  <div class="contact-photo abs" role="img" aria-label="Light room with arc lamp, small table and plants"></div>
  <h2 class="contact-title abs serif">CONTACT US</h2>
  <p class="contact-sub abs">Lorem Ipsum is simply dummy text of the printing and typesetting industry.</p>
  <span class="field-label" style="left:640px;top:2926px">First name</span>
  <div class="field" style="left:640px;top:2942px;width:222px;height:36px"></div>
  <span class="field-label" style="left:878px;top:2926px">Last name</span>
  <div class="field" style="left:878px;top:2942px;width:222px;height:36px"></div>
  <span class="field-label" style="left:640px;top:3000px">Email address</span>
  <div class="field" style="left:640px;top:3016px;width:460px;height:36px"></div>
  <span class="field-label" style="left:640px;top:3068px">Message</span>
  <div class="field" style="left:640px;top:3084px;width:460px;height:116px"></div>
  <a class="submit-btn btn">Submit now</a>
</section>

<footer class="site-footer abs">
  <div class="footer-brand abs"><span class="brand-mark"></span><span class="brand-name">Lumaform</span></div>

  <h3 class="footer-head" style="left:408px">CONTACT US</h3>
  <ul class="footer-list contact-list" style="left:408px">
    <li><svg viewBox="0 0 12 12"><path d="M6 11 C2 6 2 5 2 4.5 A4 4 0 0 1 10 4.5 C10 5 10 6 6 11 Z"/><circle cx="6" cy="4.5" r="1.3"/></svg>Fjordveien 14</li>
    <li><svg viewBox="0 0 12 12"></svg>7713 Lysvik</li>
    <li><svg viewBox="0 0 12 12"><path d="M2 1 H5 L6 4 L4 5 Q5 8 7 8 L8 6 L11 7 V10 Q5 11 1 2 Z"/></svg>+47 400 12 345</li>
    <li><svg viewBox="0 0 12 12"><rect x="1" y="2.5" width="10" height="7"/><path d="M1 2.5 L6 7 L11 2.5"/></svg>post@lumaform-example.no</li>
  </ul>

  <h3 class="footer-head" style="left:652px">QUICK LINKS</h3>
  <ul class="footer-list" style="left:652px">
    <li>Home</li><li>About Lumaform</li><li>Services and prices</li><li>Contact us</li>
  </ul>

  <h3 class="footer-head" style="left:888px">FOLLOW US</h3>
  <div class="social"><span></span><span></span><span></span><span></span></div>

  <div class="footer-rule abs"></div>
  <p class="copyright abs">Copyright © 2020 | Lumaform. All Rights Reserved.</p>
</footer>

</body>
</html>
```